Dana's Business Card Design

I am in need of a business card design for our company Tolleshunt Wrecking & Reclaim (WA) Pty Ltd. Apart from being licenced demolition contractors for residential, commercial or industrial projects we have a 20 acre salvage yard full of recycled building materials, we are also licenced to remove Asbestos and we have our own recycling/refuge tip and this site is also licenced to take Asbestos contamination landfill,we also have a sandpit in which we sell sand. Our primary colour is blue and we have a little man logo which i will attach that has been our logo for the good part of the last thirty years so this is to be included, I wont mind if you alter/update him in any way although his tattoo's must remain.
Target Market(s)
Construction & Building Industry
Industry/Entity Type
Industrial
Contact Information for Business Card
TOLLESHUNT WRECKING & RECLAIM (WA) PTY LTD
Dana Tolleshunt
Credit Controller/Payroll Officer
2417 Felmore Ridge Road
LOWER ELDERGATE  WA  6071
PH: 0428 615 704
Fax: (08) 9371 5820
dana@twreck.example.com.au
tolleshuntwrecking.example.com.au

```html
<!DOCTYPE html>
<html lang="en">
<head>
<meta charset="utf-8">
<title>Dana Tolleshunt – Business Card</title>
<link rel="stylesheet" href="https://fonts.googleapis.com/css2?family=PT+Sans&display=swap">
<style>
  :root {
    --bg-centre: #2a2f32;
    --bg-edge: #0b0d0e;
    --text-light: #f2f2f2;
    --text-muted: #a9b1b3;
    --icon: #b9c0c2;
    --divider: #3a4043;
    --mascot-light: #8d9091;
    --mascot-dark: #5b5e60;
  }
  html, body {
    margin: 0;
    padding: 0;
    overflow: hidden;
    background: #000;
  }
  .card {
    position: relative;
    width: 1200px;
    height: 686px;
    overflow: hidden;
    background: radial-gradient(ellipse 70% 65% at 50% 40%, var(--bg-centre) 0%, #1a1e20 55%, var(--bg-edge) 100%);
    font-family: "PT Sans", "Myriad Pro", sans-serif;
  }
  .contact-list {
    position: absolute;
    right: 574px;
    top: 0;
    margin: 0;
    padding: 0;
    list-style: none;
    text-align: right;
    color: var(--text-light);
    font-size: 25px;
    line-height: 1;
  }
  .contact-list li {
    position: absolute;
    right: 0;
    white-space: nowrap;
  }
  .contact-mobile  { top: 258px; }
  .contact-address { top: 305px; font-size: 23px; }
  .contact-web     { top: 351px; }
  .contact-fax     { top: 399px; }
  .contact-email   { top: 456px; }
  .divider {
    position: absolute;
    left: 646px;
    top: 234px;
    width: 2px;
    height: 258px;
    background: var(--divider);
  }
  .icon {
    position: absolute;
    width: 34px;
    height: 34px;
    left: 672px;
    fill: var(--icon);
    stroke: none;
  }
  .icon-phone    { top: 253px; }
  .icon-pin      { top: 300px; }
  .icon-mail     { top: 350px; }
  .icon-mobile   { top: 396px; height: 44px; }
  .icon-at       { top: 461px; width: 40px; height: 40px; left: 669px; }
  .job-title {
    position: absolute;
    left: 731px;
    top: 312px;
    margin: 0;
    font-size: 27px;
    font-weight: 400;
    color: var(--text-muted);
    white-space: nowrap;
  }
  .mascot {
    position: absolute;
    left: 1034px;
    top: 189px;
    width: 134px;
    height: 223px;
    border-radius: 48% 48% 30% 30%;
    background: linear-gradient(160deg, var(--mascot-light), var(--mascot-dark));
    opacity: 0.85;
  }
</style>
</head>
<body>
<main class="card">
  <ul class="contact-list">
    <li class="contact-mobile">0428 615 704</li>
    <li class="contact-address">2417 Felmore Ridge Road LOWER ELDERGATE WA 6071</li>
    <li class="contact-web">tolleshuntwrecking.example.com.au</li>
    <li class="contact-fax">(08) 9371 5820</li>
    <li class="contact-email">dana@twreck.example.com.au</li>
  </ul>

  <div class="divider"></div>

  <svg class="icon icon-phone" viewBox="0 0 34 34" aria-hidden="true">
    <path d="M3 12c0-5 6-7 14-7s14 2 14 7v3h-7v-4h-14v4H3z"/>
    <path d="M7 16h20l3 12H4z"/>
    <circle cx="17" cy="22" r="3.5" fill="#1e2325"/>
  </svg>

  <svg class="icon icon-pin" viewBox="0 0 34 34" aria-hidden="true">
    <path d="M17 2a10 10 0 0 0-10 10c0 8 10 20 10 20s10-12 10-20A10 10 0 0 0 17 2zm0 14a4 4 0 1 1 0-8 4 4 0 0 1 0 8z"/>
  </svg>

  <svg class="icon icon-mail" viewBox="0 0 34 34" aria-hidden="true">
    <path d="M2 8h30v19H2z"/>
    <path d="M2 8l15 11L32 8" fill="none" stroke="#1e2325" stroke-width="2"/>
  </svg>

  <svg class="icon icon-mobile" viewBox="0 0 34 44" aria-hidden="true">
    <rect x="8" y="2" width="20" height="40" rx="3"/>
    <rect x="11" y="6" width="14" height="14" fill="#1e2325"/>
    <g fill="#1e2325">
      <circle cx="13" cy="26" r="1.6"/><circle cx="18" cy="26" r="1.6"/><circle cx="23" cy="26" r="1.6"/>
      <circle cx="13" cy="31" r="1.6"/><circle cx="18" cy="31" r="1.6"/><circle cx="23" cy="31" r="1.6"/>
      <circle cx="13" cy="36" r="1.6"/><circle cx="18" cy="36" r="1.6"/><circle cx="23" cy="36" r="1.6"/>
    </g>
    <rect x="4" y="8" width="2" height="30"/>
  </svg>

  <svg class="icon icon-at" viewBox="0 0 40 40" aria-hidden="true">
    <path d="M20 3a17 17 0 1 0 9 31.4l-1.4-2.4A14 14 0 1 1 34 20v2a3 3 0 0 1-6 0V12h-3v1.5a8 8 0 1 0 .7 11.3A6 6 0 0 0 37 22v-2A17 17 0 0 0 20 3zm0 22a5 5 0 1 1 0-10 5 5 0 0 1 0 10z"/>
  </svg>

  <p class="job-title">Controller/Payroll Officer</p>

  <div class="mascot" role="img" aria-label="Company mascot: the little workman with hammer, shown faded in grey"></div>
</main>
</body>
</html>
```